Corvallin Property Solutions need a business card design

Hello guys. We would need a business card design asap please.
We are a start up property investment business based in London UK specialised in buying, selling, managing and letting properties and helping distressed property owners.
The name of our Business is Corvallin, the logo symbolises the four fundamental elements of the world (earth, air, fire and water) and so it stands for strength, stability, longevity.
We would like the business card to communicate professionalism and reliability. Many many thanks indeed for your work.

Details:

1.) Marisol Dunkley
Property Investor
Mobile: +44(0)7700362517
Email: marisol.corvallin@quilbrook.example

2.) Tomas Brindle
Property Investor
Mobile: +44(0)7700845926
Email: tomas.corvallin@quilbrook.example

Industry/Entity Type

Investment

```html
<!DOCTYPE html>
<html lang="en">
<head>
<meta charset="utf-8">
<title>Corvallin Property Solutions – Business Card</title>
<link href="https://fonts.googleapis.com/css2?family=Jost:wght@500;600&family=Open+Sans:wght@400;600&display=swap" rel="stylesheet">
<style>
  :root {
    --red: #bc2a35;
    --green: #1f6b3b;
    --blue: #2d52a8;
    --ink: #1c1c1c;
    --white: #ffffff;
    --backdrop: #e4e5e7;
  }
  * { box-sizing: border-box; margin: 0; padding: 0; }
  html, body {
    width: 1200px; height: 987px; overflow: hidden;
    background: var(--backdrop);
  }
  .canvas { position: relative; width: 1200px; height: 987px; }
  .card {
    position: absolute; left: 320px;
    width: 560px; height: 320px;
    border-radius: 26px; overflow: hidden;
  }
  /* Back side */
  .card-back {
    top: 130px; background: var(--red);
    display: flex; align-items: center; justify-content: center;
  }
  .card-back .wordmark {
    font-family: "Jost", sans-serif; font-weight: 600;
    color: var(--white); text-align: center; line-height: 1.05;
    letter-spacing: 0.04em;
  }
  .card-back .wordmark .name { display: block; font-size: 58px; }
  .card-back .wordmark .tagline { display: block; font-size: 24px; letter-spacing: 0.08em; }

  /* Front side */
  .card-front { top: 530px; background: var(--white); }
  .card-front .wave { position: absolute; inset: 0; width: 560px; height: 320px; }
  .brand {
    position: absolute; left: 200px; top: 52px;
    display: flex; align-items: center; gap: 14px;
  }
  .brand .mark { width: 34px; height: 34px; background: var(--red); }
  .brand .wordmark {
    font-family: "Jost", sans-serif; font-weight: 600;
    color: var(--ink); line-height: 1.05; letter-spacing: 0.04em;
  }
  .brand .wordmark .name { display: block; font-size: 30px; }
  .brand .wordmark .tagline { display: block; font-size: 12.5px; letter-spacing: 0.08em; }

  .holder {
    position: absolute; left: 30px; top: 220px;
    font-family: "Open Sans", sans-serif; color: var(--white);
  }
  .holder .person { font-size: 17px; font-weight: 600; line-height: 1.3; }
  .holder .role { font-size: 13px; font-weight: 400; line-height: 1.3; margin-top: 2px; }

  .contact {
    position: absolute; right: 34px; bottom: 20px;
    font-family: "Open Sans", sans-serif; color: var(--white);
    font-size: 14px; line-height: 1.3; text-align: right; list-style: none;
  }
  .contact li { display: flex; align-items: center; justify-content: flex-end; gap: 8px; margin-top: 6px; }
  .contact svg { width: 14px; height: 14px; fill: var(--white); }
</style>
</head>
<body>
<main class="canvas">
  <section class="card card-back" aria-label="Card back">
    <h1 class="wordmark">
      <span class="name">CORVALLIN</span>
      <span class="tagline">PROPERTY SOLUTIONS</span>
    </h1>
  </section>

  <section class="card card-front" aria-label="Card front">
    <svg class="wave" viewBox="0 0 560 320" aria-hidden="true">
      <defs>
        <path id="swoosh" d="M0,105 C40,168 120,200 240,218 C360,234 470,232 560,224 L560,340 L0,340 Z"/>
      </defs>
      <use href="#swoosh" fill="var(--blue)" transform="translate(0,-14)"/>
      <use href="#swoosh" fill="var(--white)" transform="translate(0,-10)"/>
      <use href="#swoosh" fill="var(--green)" transform="translate(0,-7)"/>
      <use href="#swoosh" fill="var(--white)" transform="translate(0,-3)"/>
      <use href="#swoosh" fill="var(--red)"/>
    </svg>

    <div class="brand">
      <span class="mark" aria-hidden="true"></span>
      <p class="wordmark">
        <span class="name">CORVALLIN</span>
        <span class="tagline">PROPERTY SOLUTIONS</span>
      </p>
    </div>

    <div class="holder">
      <p class="person">Tomas Brindle</p>
      <p class="role">Property Investor</p>
    </div>

    <ul class="contact">
      <li>
        <svg viewBox="0 0 16 16" aria-hidden="true"><path d="M4 0h8a1 1 0 0 1 1 1v14a1 1 0 0 1-1 1H4a1 1 0 0 1-1-1V1a1 1 0 0 1 1-1zm1 2v9h6V2zm3 10.5a1 1 0 1 0 0 2 1 1 0 0 0 0-2z"/></svg>
        <span>+44(0)7700845926</span>
      </li>
      <li>
        <svg viewBox="0 0 16 16" aria-hidden="true"><path d="M1 3h14v10H1zm1.5 1.2V12h11V4.2L8 8.5z"/></svg>
        <span>tomas.corvallin@quilbrook.example</span>
      </li>
    </ul>
  </section>
</main>
</body>
</html>
```